Marketing Expert Needs a Book Cover Design to Inspire Audiences

Need a book cover design for my first book!
The book is a ‘How To’ serious non fiction book. It has insights for marketers on how to transform their marketing to help their organizations accelerate sales and drive growth. This is not a high level theoretical book about brand building. Instead this includes strategic frameworks, and tried and tested ideas and tactics which marketers (or aspiring marketers) can use to be successful in their jobs. The premise of this book is that it’s no longer enough for marketers to focus on brand recognition. We need to help the business to create demand and make it easier for our sales colleagues to close deals.
The aim is to inspire readers with insights so that they think differently about themselves and their marketing. The aim is to compel them to take start new conversations to accelerate sales, using the tools, concepts and case studies outlined in the book.
The Title: The Growth Signal
Subtitle: Steps to Win Buyers by Storytelling, Curiosity and Trusted Voices.
The cover must have a compelling visual which communicates this idea-
The Growth Signal Inspires You to Think Different so That You Scale/Overcome the Limits you might have placed on yourself or your business.
I like a simple and clean look. I'm attaching some samples which I like. Looking to achieve the same look for my book cover.
Update- I need the cover for an ebook only. Since the cover will be displayed as a thumbnail in Verbolt and other online shopping sites, it should be without any clutter with good contrast between images and text. This will help with visibility.
Updates
Key Art Style designs will also be welcome. Added Saturday, September 24, 2016
Reason: I'm hoping that atleast some more top 20 designers will respond.
Target Market(s)
Target market is CMOs, Marketing Managers, Business Leaders, MBA students- anyone who is looking to reshape and rejig their marketing skills and teams.
Industry/Entity Type
Marketing
Requirements
Must have
- A compelling visual is a must have.
- It shouldn't have only text.
Nice to have
- Please refer the cover samples I sent.
- Key Art designs will also be welcome.
Should not have
- Clutter.
- I like simplicity.

```html
<!DOCTYPE html>
<html lang="en">
<head>
<meta charset="utf-8">
<title>The Growth Signal — Book Cover</title>
<link rel="stylesheet" href="https://fonts.googleapis.com/css2?family=Oswald:wght@500;600&family=Caladea&display=swap">
<style>
  :root {
    --page-bg: #ffffff;
    --cover-yellow: #f6ea2b;
    --bubble-blue: #2a5ea6;
    --title-blue: #0b54a2;
    --ink-blue: #1d4f9a;
    --shadow: rgba(0, 0, 0, 0.18);
  }
  * { box-sizing: border-box; margin: 0; padding: 0; }
  html, body {
    width: 1200px;
    height: 1135px;
    overflow: hidden;
    background: var(--page-bg);
  }
  .canvas {
    position: relative;
    width: 1200px;
    height: 1135px;
  }
  .cover {
    position: absolute;
    left: 260px;
    top: 26px;
    width: 680px;
    height: 1082px;
    background: var(--cover-yellow);
    box-shadow: 0 6px 18px var(--shadow);
    overflow: hidden;
  }
  .speech-bubble {
    position: absolute;
    inset: 0;
    width: 100%;
    height: 100%;
  }
  .speech-bubble path { fill: var(--bubble-blue); }
  .book-title { font-size: inherit; font-weight: inherit; }
  .title {
    position: absolute;
    left: 0;
    width: 100%;
    text-align: center;
    font-family: "Oswald", sans-serif;
    font-weight: 600;
    text-transform: uppercase;
    line-height: 1;
  }
  .title-article {
    top: 84px;
    font-size: 62px;
    color: var(--cover-yellow);
    transform: rotate(-3deg);
  }
  .title-bubble-word {
    left: 20px;
    top: 168px;
    font-size: 146px;
    letter-spacing: 0;
    color: var(--cover-yellow);
    transform: rotate(-3deg) scaleY(1.45);
    transform-origin: center top;
  }
  .title-main-word {
    top: 548px;
    font-size: 196px;
    letter-spacing: 3px;
    color: var(--title-blue);
    transform: scaleY(0.95);
    transform-origin: center top;
  }
  .subtitle {
    position: absolute;
    left: 40px;
    right: 40px;
    top: 792px;
    text-align: center;
    font-family: "Caladea", serif;
    font-size: 35px;
    line-height: 1.08;
    color: var(--ink-blue);
  }
  .author {
    position: absolute;
    left: 0;
    width: 100%;
    top: 960px;
    text-align: center;
    font-family: "Oswald", sans-serif;
    font-weight: 500;
    font-size: 50px;
    letter-spacing: 0.5px;
    text-transform: uppercase;
    color: var(--title-blue);
    transform: scaleY(1.05);
  }
</style>
</head>
<body>
  <main class="canvas">
    <article class="cover">
      <svg class="speech-bubble" viewBox="0 0 710 1130" preserveAspectRatio="none" aria-hidden="true">
        <path d="M58 73 L652 16 Q684 13 681 45 L645 428 Q642 458 612 460 L347 452 L222 570 L250 446 L98 437 Q70 435 66 407 L30 104 Q27 76 58 73 Z"/>
      </svg>
      <h1 class="book-title">
        <span class="title title-article">The</span>
        <span class="title title-bubble-word">Growth</span>
        <span class="title title-main-word">Signal</span>
      </h1>
      <p class="subtitle">Steps to Win Buyers<br>by Storytelling, Curiosity<br>and Trusted Voices.</p>
      <p class="author">Author Name</p>
    </article>
  </main>
</body>
</html>
```